Clean/luxurious/food site. Work should be completed this weekend

Project Description:
This is a flash work. The design must be clean and ready by the end of the weekend.
I will provide full 24hr support to give feedback and get it ready.
Final product must be the final PSD files with all the design blocks, complete CSS, and links programed into the files.
The work is simple and straight forward, the design structure should be just the 5 elements presented.
What do you do?
The basic idea: We are a highend catering platform.
We provide a better way to discover, compare, and order catering from local restaurants, high end caterers, and chefs.

The basic platform structure
Each Caterer will have a simple and clean profile page which will contain
• Basic details of the Caterer
1. Purveyor
2. Cuisine
3. Amount of Food
4. Price Per Person
5. Min Order
6. Max Order
7. Notice Required
ORDER BOX- where users decide the amount of the order base on the # of people and price per person

• Slideshow for picture of food provided (max 5 pictures)
• A short text box for the description of the food and the delivery options
• The feedback that the caterer has received from clients
• Basic badge system (based on the 5 star rating)

The SITE WILL BE IN SPANISH. Our target market is found in Latinamerica
Do you have a desired website screen size?
Full screen ( optimized for a 13 Inch screen)
How many pages (maximum of 5) do you need designed?
5 pages (1- Landing page) (2-Signup process (max 3 step signup process) (3-Caterer individual profile page) (4-Search page) (5-Static page Full left sidebar)
What is your industry?
We are in the restaurant, food and luxury high end industry
Describe the target audience for your website design
Site will be in spanish. Target audience in LatinAmerica.. age 16-29, women, urban, speak Spanish and English are active on social networks and like extracurricular activities.

What 3 things would you like to communicate to your audience through your website design
Find great private catarers
The best food in town
Simple and secure
Clean
The best match
How is your company different from your competitors?
Clean simple design to search by date or reference the best match
Free service
Luxurious touch
backed by the best on the industry
What website design styles do you like?
Inspiration for Landing Page
http://plumbrix.com/

The concept

https://www.dishwarren.com/

The landing page
http://plumbrix.com/

The signup for chefs
https://www.tavello.com/chef_applications/new
https://www.dishwarren.com/packages/new

The inner pages

https://www.dishwarren.com/collections/11-personal-touch
MerlowBay.com https://www.tavello.com/

What colors do you want to see in your website design?
•Different types of blue (light blue) or orange
No more than 2 colors
white/earth
light green
• Use the codenest fromtwitter scaffold design (http://quibbler.codenest.com/scaffold/)
What colors do you NOT want to see in your website design?
Black-pink-red-yellow
What adjectives should best describe your website design?
clean
bold
bright
texture
What content must be included in the website design?
landing page with no more than 3 elements, very clean and simple
Landing page should have either have a central space for main tagline or a broken 2 sided box must have a bottom footer to have the basic navigation links (like merlowbay.com)
Use of simple and clean icons
Top right space for small logo
Use of helvetica or clean modern font
inner pages with a simple structure and a left sidebar to add a few elements of navigation
inner pages should have an upper slim banner for navigation bar or breadcrumbs
Do you have additional requirements or links you want to share?
• Use the codenest from quibbler scaffold design (http://quibbler.codenest.com/scaffold/)

ONLY SERIOUS ABOUT DESIGN AND FINISH THIS WEEKEND

```html
<!DOCTYPE html>
<html lang="en">
<head>
<meta charset="utf-8">
<title>Catering Landing</title>
<link rel="stylesheet" href="https://fonts.googleapis.com/css2?family=Federo&family=Courgette&family=Noto+Sans:wght@400&display=swap">
<style>
  :root {
    --ink-green: #2e4420;
    --logo-green: #2f4a22;
    --button-green: #6e8f5e;
    --close-green: #aac3a2;
    --text-grey: #4a4a4a;
    --link-grey: #6a6a6a;
    --field-border: #d4d4d4;
    --panel: rgba(255, 255, 255, 0.84);
    --band: rgba(255, 255, 255, 0.8);
    --white: #ffffff;
  }
  * { box-sizing: border-box; margin: 0; padding: 0; }
  html, body { width: 1200px; height: 800px; overflow: hidden; }
  body { position: relative; font-family: "Noto Sans", Verdana, sans-serif; background: #2a1a12; }

  .hero-photo {
    position: absolute; inset: 0;
    background:
      radial-gradient(circle at 1030px 220px, #f7dca0 0, #e9b56a 120px, rgba(150,90,40,0) 260px),
      radial-gradient(ellipse 520px 300px at 600px 460px, #e8e3dc 0, #cfc7bc 55%, rgba(120,90,70,0) 100%),
      radial-gradient(ellipse 260px 200px at 360px 220px, #6a4a2a 0, rgba(90,60,35,0) 100%),
      linear-gradient(180deg, #3a2418 0%, #4a2e1c 45%, #24160f 100%);
  }

  .site-header {
    position: absolute; left: 0; top: 72px; width: 1200px; height: 88px;
    background: var(--band);
  }
  .brand {
    position: absolute; left: 155px; top: 92px;
    font-family: "Federo", sans-serif; font-size: 46px; line-height: 1;
    color: var(--logo-green);
  }
  .main-nav a {
    position: absolute; top: 106px;
    font-family: "Courgette", cursive; font-size: 17px;
    color: #4a5a3a; text-decoration: none;
  }
  .main-nav a.is-current { text-decoration: underline; }

  .welcome-panel {
    position: absolute; left: 198px; top: 186px; width: 800px; height: 450px;
    background: var(--panel); border-radius: 2px;
  }
  .close-button {
    position: absolute; right: 0; top: 0; width: 37px; height: 32px;
    background: var(--close-green); color: var(--white);
    font-size: 22px; line-height: 32px; text-align: center;
  }
  .panel-title {
    position: absolute; font-family: "Courgette", cursive; font-weight: 400;
    font-size: 23px; color: var(--ink-green);
  }
  .panel-title strong { font-weight: 400; text-shadow: 0.6px 0 0 var(--ink-green); }
  .intro-text {
    position: absolute; left: 32px; top: 61px; width: 331px;
    font-size: 14px; line-height: 28px; color: var(--text-grey);
    text-align: justify; letter-spacing: 0.15px;
  }
  .button {
    position: absolute; height: 41px;
    background: var(--button-green); color: var(--white);
    font-size: 18px; line-height: 41px; text-align: center;
    border: 1px solid #e8eee4; box-shadow: 0 0 0 1px rgba(0,0,0,0.05);
  }
  .field {
    position: absolute; left: 403px; width: 339px; height: 40px;
    background: var(--white); border: 1px solid var(--field-border); border-radius: 3px;
    padding-left: 9px; font-size: 14px; line-height: 38px; color: #7a7a7a;
  }
  .forgot-link {
    position: absolute; left: 407px; top: 187px;
    font-size: 14px; color: var(--link-grey); text-decoration: underline;
  }
  .tagline {
    position: absolute; left: 410px; top: 322px; width: 350px;
    font-family: "Courgette", cursive; font-style: italic;
    font-size: 21px; line-height: 30px; color: var(--ink-green);
  }

  .dish-strip { position: absolute; left: 388px; top: 669px; display: flex; gap: 16px; }
  .dish {
    width: 74px; height: 74px; border-radius: 50%;
    border: 2px solid #e8e8e8;
  }
</style>
</head>
<body>
  <div class="hero-photo" role="img" aria-label="Photograph of a plated fine-dining dish on a white plate with warm candle light"></div>

  <header class="site-header"></header>
  <div class="brand">Logo Here</div>
  <nav class="main-nav">
    <a class="is-current" href="#" style="left:542px">Home</a>
    <a href="#" style="left:628px">What we do</a>
    <a href="#" style="left:758px">Caterers</a>
    <a href="#" style="left:861px">Menu</a>
    <a href="#" style="left:944px">Contact Us</a>
  </nav>

  <section class="welcome-panel">
    <div class="close-button">X</div>

    <h2 class="panel-title" style="left:29px;top:20px"><strong>Welcome</strong> to our site</h2>
    <p class="intro-text">We are the onest fine manager togather all caterers at your service to richen up customers taste at the top lavel, we proud of this. We are the onest fine manager togather all caterers at your service to richen up customers taste at the top lavel, we proud of this.<br>We are the onest fine manager togather all caterers at your service to richen up customers taste at the top lavel, we proud of this.We are the onest fine manager togather all caterers at your service to richen up.</p>
    <a class="button" href="#" style="left:31px;top:385px;width:132px">Know More</a>

    <h2 class="panel-title" style="left:404px;top:22px"><strong>Client</strong> Login</h2>
    <div class="field" style="top:66px">User name</div>
    <div class="field" style="top:116px">Password</div>
    <a class="forgot-link" href="#">Forget Password?</a>
    <a class="button" href="#" style="left:610px;top:176px;width:133px">Submit</a>

    <h2 class="panel-title" style="left:405px;top:250px"><strong>New</strong> Member?</h2>
    <a class="button" href="#" style="left:610px;top:246px;width:133px">Sign Up</a>

    <p class="tagline">To get our easy to reach customers all over the country.</p>
  </section>

  <div class="dish-strip">
    <div class="dish" role="img" aria-label="Photo of a wrap with greens" style="background:radial-gradient(circle,#7a5a3a,#cfc8c0)"></div>
    <div class="dish" role="img" aria-label="Photo of a layered chocolate cake slice" style="background:radial-gradient(circle,#6a3a22,#e2d6c8)"></div>
    <div class="dish" role="img" aria-label="Photo of a salad with berries" style="background:radial-gradient(circle,#5a6a2a,#2a1e14)"></div>
    <div class="dish" role="img" aria-label="Photo of a plated meat dish" style="background:radial-gradient(circle,#8a6a4a,#d8d0c4)"></div>
    <div class="dish" role="img" aria-label="Photo of sushi rolls" style="background:radial-gradient(circle,#e8e0d0,#b89070)"></div>
  </div>
</body>
</html>
```